Customer Quotes Page

We want to create a fun looking customer quotes page. The point of this project is to be get creative with the treatment of the quotes. Our current version of the page just has them listed in two columns, which is pretty boring. We need something more interesting but it should still fit into our site. Attached is the current Testimonials page as it looks now. The two column layout does not have to be maintained, you can list the manager quotes above the resident quotes. Also not all quotes have to be used, we just need to see 5-10 from the resident and management categories.
The header and footer is already designed, so those elements need to stay the same. The background color also needs to remain same (light fuzzy gray)
Here is a site that we like: https://plumcrestapp.com/about/ (take a look at the "What people are saying" section). But this is just an example, we might like something radically different. The point is to be as creative with the quote boxes as possible. A very refined but subdued approach might also be interesting.
FINAL FILE SHOULD BE A PSD FILE WITH LAYERS. WE WILL CODE THE PAGE OURSELVES.
What we're most interested in this contest is the graphic treatment of the quotes. Right now they're simply gray boxes. We'd like to see what you can do with this. The layout of the page can remain same (two-column) but a 1 column layout is also fine. Also please don't add any additional elements to the page like stock photo. We are only interested in the treatment of the quotes and anything goes whether it is very elegant, cartoony, bold and colorful, hand-drawn, 3D, textured......

```html
<!DOCTYPE html>
<html lang="en">
<head>
<meta charset="utf-8">
<title>Testimonial – Tenantry</title>
<link href="https://fonts.googleapis.com/css2?family=Source+Sans+3:ital,wght@0,400;0,600;1,400;1,700&display=swap" rel="stylesheet">
<style>
:root{
  --page-bg:#f1f1f1;
  --nav-top:#474747;
  --nav-bottom:#1f1f1f;
  --nav-divider:#5a5a5a;
  --nav-text:#ffffff;
  --cta-top:#f2a80a;
  --cta-bottom:#8a5a05;
  --heading-red:#c9202c;
  --note-yellow:#fbe87a;
  --quote-text:#3b3522;
  --pin-red:#e0153a;
  --pin-dark:#a0071f;
}
*{box-sizing:border-box;margin:0;padding:0}
html,body{width:1200px;height:900px;overflow:hidden}
body{
  background:var(--page-bg);
  font-family:"Source Sans 3","Myriad Pro",Arial,sans-serif;
  position:relative;
}
.site-nav{
  position:absolute;left:0;top:0;width:1200px;height:55px;
  background:linear-gradient(var(--nav-top),var(--nav-bottom));
}
.nav-list{position:absolute;left:91px;top:0;display:flex;list-style:none;height:55px;border-left:1px solid var(--nav-divider)}
.nav-item{
  width:128px;height:55px;border-right:1px solid var(--nav-divider);
  display:flex;align-items:center;justify-content:center;text-align:center;
  color:var(--nav-text);font-size:15px;line-height:20px;position:relative;
}
.nav-item.is-active::after{
  content:"";position:absolute;left:52px;bottom:-11px;
  border-left:11px solid transparent;border-right:11px solid transparent;
  border-top:11px solid var(--nav-bottom);
}
.nav-item.is-cta{
  background:linear-gradient(var(--cta-top),var(--cta-bottom));
  font-weight:600;text-shadow:0 1px 1px rgba(0,0,0,.5);
}
.page-title{
  position:absolute;left:91px;top:86px;
  color:var(--heading-red);font-size:24px;font-weight:400;letter-spacing:-.2px;
}
.column-title{
  position:absolute;top:141px;color:var(--heading-red);font-size:18px;font-weight:400;
}
.quote-note{position:absolute;width:501px}
.note-paper{position:absolute;left:0;top:0;overflow:visible}
.note-body{position:relative;padding:49px 40px 0 23px}
.note-quote{
  font-style:italic;font-size:15.2px;line-height:19.4px;color:var(--quote-text);
}
.note-author{
  margin-top:12px;font-style:italic;font-weight:700;font-size:11px;color:var(--quote-text);
}
.push-pin{position:absolute;left:232px;top:-19px}
</style>
</head>
<body>
<svg width="0" height="0" style="position:absolute">
  <defs>
    <filter id="curl-blur" x="-20%" y="-100%" width="140%" height="300%">
      <feGaussianBlur stdDeviation="3.5"/>
    </filter>
    <linearGradient id="curl-right" x1="0" x2="1" y1="0" y2="0">
      <stop offset="0" stop-color="#000" stop-opacity="0"/>
      <stop offset=".6" stop-color="#000" stop-opacity=".45"/>
      <stop offset="1" stop-color="#000" stop-opacity=".7"/>
    </linearGradient>
    <linearGradient id="curl-left" x1="0" x2="1" y1="0" y2="0">
      <stop offset="0" stop-color="#000" stop-opacity=".7"/>
      <stop offset=".45" stop-color="#000" stop-opacity=".45"/>
      <stop offset="1" stop-color="#000" stop-opacity="0"/>
    </linearGradient>
    <radialGradient id="pin-head" cx="38%" cy="32%" r="70%">
      <stop offset="0" stop-color="#ff7a90"/>
      <stop offset=".45" stop-color="#e0153a"/>
      <stop offset="1" stop-color="#9a061c"/>
    </radialGradient>
    <symbol id="pin" viewBox="0 0 40 50">
      <ellipse cx="17" cy="40" rx="9" ry="3" fill="rgba(0,0,0,.18)"/>
      <path d="M8 28 Q15 24 25 27 Q26 36 17 41 Q9 38 8 28 Z" fill="url(#pin-head)"/>
      <path d="M15 14 H24 L23 28 H16 Z" fill="#c80f2f"/>
      <circle cx="20" cy="13" r="11" fill="url(#pin-head)"/>
      <ellipse cx="16" cy="8" rx="4.5" ry="2.8" fill="#ffd5dc" opacity=".85"/>
    </symbol>
  </defs>
</svg>

<header class="site-nav">
  <ul class="nav-list">
    <li class="nav-item">Home</li>
    <li class="nav-item">About<br>Tenantry</li>
    <li class="nav-item">Management<br>Experience</li>
    <li class="nav-item">Resident<br>Experience</li>
    <li class="nav-item">Technology<br>&amp; Innovation</li>
    <li class="nav-item is-active">Testimonial</li>
    <li class="nav-item">Support</li>
    <li class="nav-item is-cta">Request<br>Demo</li>
  </ul>
</header>

<h1 class="page-title">TESTIMONIAL</h1>
<h2 class="column-title" style="left:91px">MANAGER QUOTES</h2>
<h2 class="column-title" style="left:613px">RESIDENT QUOTES</h2>

<!-- Row 1 -->
<article class="quote-note" style="left:91px;top:178px">
  <svg class="note-paper" width="501" height="215">
    <path d="M240 200 Q400 195 496 174 L499 184 Q410 206 260 205 Z" fill="url(#curl-right)" filter="url(#curl-blur)"/>
    <path d="M0 0 H501 V172 Q300 196 0 200 Z" fill="var(--note-yellow)"/>
  </svg>
  <svg class="push-pin" width="40" height="50"><use href="#pin"/></svg>
  <div class="note-body">
    <p class="note-quote">“ Lorem ipsum dolor sit amet, consectetur adipiscing elit. Duis ac lorem vitae metus consectetur ultricies ut vitae metus. Duis in libero a sem bibendum aliquam. Nunc tempus, lacus non sagittis gravida, felis lorem molestie lacus, et ullamcorper neque mauris in nulla.”</p>
    <p class="note-author">Maya L, Manager, Halden At The Larchmont</p>
  </div>
</article>
<article class="quote-note" style="left:614px;top:178px">
  <svg class="note-paper" width="501" height="215">
    <path d="M240 200 Q400 195 496 174 L499 184 Q410 206 260 205 Z" fill="url(#curl-right)" filter="url(#curl-blur)"/>
    <path d="M0 0 H501 V172 Q300 196 0 200 Z" fill="var(--note-yellow)"/>
  </svg>
  <svg class="push-pin" width="40" height="50"><use href="#pin"/></svg>
  <div class="note-body">
    <p class="note-quote">“ Lorem ipsum dolor sit amet, consectetur adipiscing elit. Duis ac lorem vitae metus consectetur ultricies ut vitae metus. Duis in libero a sem bibendum aliquam. Nunc tempus, lacus non sagittis gravida, felis lorem molestie lacus, et ullamcorper neque mauris in nulla.”</p>
    <p class="note-author">Maya L, Manager, Halden At The Larchmont</p>
  </div>
</article>

<!-- Row 2 -->
<article class="quote-note" style="left:91px;top:405px">
  <svg class="note-paper" width="501" height="300">
    <path d="M6 260 Q150 279 440 284 L420 290 Q160 292 12 272 Z" fill="url(#curl-left)" filter="url(#curl-blur)"/>
    <path d="M0 0 H501 V283 Q200 280 0 256 Z" fill="var(--note-yellow)"/>
  </svg>
  <svg class="push-pin" width="40" height="50"><use href="#pin"/></svg>
  <div class="note-body">
    <p class="note-quote">“Lorem ipsum dolor sit amet, consectetur adipiscing elit. Duis ac lorem vitae metus consectetur ultricies ut vitae metus. Duis in libero a sem bibendum aliquam. Nunc tempus, lacus non sagittis gravida, felis lorem molestie lacus, et ullamcorper neque mauris in nulla. Sed vitae nunc orci. Suspendisse ultricies, mi sit amet placerat interdum, elit orci iaculis libero, eu egestas sapien tellus sed erat. Aliquam erat volutpat. Praesent fermentum orci at nibh euismod consectetur. Nulla mi urna, feugiat eget blandit pulvinar, pretium id justo.”</p>
    <p class="note-author">Maya L, Manager, Halden At The Larchmont</p>
  </div>
</article>
<article class="quote-note" style="left:614px;top:405px">
  <svg class="note-paper" width="501" height="300">
    <path d="M6 260 Q150 279 440 284 L420 290 Q160 292 12 272 Z" fill="url(#curl-left)" filter="url(#curl-blur)"/>
    <path d="M0 0 H501 V283 Q200 280 0 256 Z" fill="var(--note-yellow)"/>
  </svg>
  <svg class="push-pin" width="40" height="50"><use href="#pin"/></svg>
  <div class="note-body">
    <p class="note-quote">“Lorem ipsum dolor sit amet, consectetur adipiscing elit. Duis ac lorem vitae metus consectetur ultricies ut vitae metus. Duis in libero a sem bibendum aliquam. Nunc tempus, lacus non sagittis gravida, felis lorem molestie lacus, et ullamcorper neque mauris in nulla. Sed vitae nunc orci. Suspendisse ultricies, mi sit amet placerat interdum, elit orci iaculis libero, eu egestas sapien tellus sed erat. Aliquam erat volutpat. Praesent fermentum orci at nibh euismod consectetur. Nulla mi urna, feugiat eget blandit pulvinar, pretium id justo.”</p>
    <p class="note-author">Maya L, Manager, Halden At The Larchmont</p>
  </div>
</article>

<!-- Row 3 -->
<article class="quote-note" style="left:91px;top:726px">
  <svg class="note-paper" width="501" height="200">
    <path d="M0 0 H501 V200 H0 Z" fill="var(--note-yellow)"/>
  </svg>
  <svg class="push-pin" width="40" height="50"><use href="#pin"/></svg>
  <div class="note-body">
    <p class="note-quote">“ Lorem ipsum dolor sit amet, consectetur adipiscing elit. Duis ac lorem vitae metus consectetur ultricies ut vitae metus. Duis in libero a sem bibendum aliquam. Nunc tempus, lacus non sagittis gravida, felis lorem molestie lacus, et ullamcorper neque mauris in nulla.”</p>
    <p class="note-author">Maya L, Manager, Halden At The Larchmont</p>
  </div>
</article>
<article class="quote-note" style="left:614px;top:726px">
  <svg class="note-paper" width="501" height="200">
    <path d="M0 0 H501 V200 H0 Z" fill="var(--note-yellow)"/>
  </svg>
  <svg class="push-pin" width="40" height="50"><use href="#pin"/></svg>
  <div class="note-body">
    <p class="note-quote">“ Lorem ipsum dolor sit amet, consectetur adipiscing elit. Duis ac lorem vitae metus consectetur ultricies ut vitae metus. Duis in libero a sem bibendum aliquam. Nunc tempus, lacus non sagittis gravida, felis lorem molestie lacus, et ullamcorper neque mauris in nulla.”</p>
    <p class="note-author">Maya L, Manager, Halden At The Larchmont</p>
  </div>
</article>
</body>
</html>
```